Bref créative
Stationary for KORVEL Trademark & Licensing
KORVEL Trademark & Licensing
Professional
Piet Morrow
VP of Technology
437 E. Alder Rd.
Larkfield, ND 58408
Piet.Morrow@korvelmarks.example
www.korvelmarks.example
Our website is not up yet, so please do not try to use this for a sample.
Our business is to trademark and licensing school logos and products. We are looking for a very professional & clean product.
I am looking for some ideas for the back our slogan "Making Your Logo Work for You" should be there somewhere.
Company Logo for KORVEL Trademark & Licensing

```html
<!DOCTYPE html>
<html lang="en">
<head>
<meta charset="utf-8">
<title>KORVEL Trademark &amp; Licensing – Business Card</title>
<link href="https://fonts.googleapis.com/css2?family=Tinos:wght@400;700&display=swap" rel="stylesheet">
<style>
  :root {
    --backdrop: #e9e6e1;
    --card: #ffffff;
    --ink: #2b2b2b;
    --rule: #b9bcc2;
    --icon: #2f6fb8;
    --band-dark: #0f3f86;
    --band-mid: #1d64c0;
    --band-light: #3f8be0;
    --band-text: #ffffff;
    --band-sub: #d6e6fb;
    --mark: #1b4f9c;
  }
  * { box-sizing: border-box; margin: 0; padding: 0; }
  html, body {
    width: 1200px; height: 965px; overflow: hidden;
    background: var(--backdrop);
    font-family: "Tinos", "Times New Roman", serif;
    color: var(--ink);
  }
  .business-card {
    position: absolute; left: 100px; top: 196px;
    width: 1000px; height: 572px;
    background: var(--card);
    border-radius: 34px;
    box-shadow: 0 10px 30px rgba(0,0,0,.18);
    overflow: hidden;
  }
  .brand {
    position: absolute; left: 44px; top: 100px;
    width: 300px;
    display: flex; align-items: center; gap: 18px;
  }
  .brand-dot {
    flex: none; width: 96px; height: 96px; border-radius: 50%;
    background: var(--mark);
  }
  .brand-name {
    font-size: 24px; line-height: 1.2; font-weight: 700; color: var(--mark);
  }
  .divider {
    position: absolute; left: 362px; top: 34px;
    width: 1px; height: 310px; background: var(--rule);
  }
  .address {
    position: absolute; left: 392px; top: 42px;
    font-size: 25px; line-height: 32px; font-style: normal;
  }
  .contact-list {
    position: absolute; left: 392px; top: 150px;
    list-style: none; font-size: 25px; line-height: 36px;
  }
  .contact-list li { display: flex; align-items: center; gap: 14px; white-space: nowrap; }
  .contact-list svg { width: 22px; height: 22px; flex: none; }
  .band-rule {
    position: absolute; left: 0; right: 0; top: 350px;
    height: 2px; background: var(--rule);
  }
  .name-band {
    position: absolute; left: 0; right: 0; top: 360px; height: 88px;
    background: linear-gradient(90deg, var(--band-dark) 0%, var(--band-mid) 30%, var(--band-light) 55%, var(--band-mid) 78%, var(--band-dark) 100%);
    text-align: center; padding-left: 180px; padding-top: 8px;
  }
  .person-name { font-size: 35px; font-weight: 700; color: var(--band-text); line-height: 40px; }
  .person-title { font-size: 25px; color: var(--band-sub); line-height: 32px; }
</style>
</head>
<body>
  <article class="business-card">
    <div class="brand">
      <span class="brand-dot"></span>
      <span class="brand-name">KORVEL Trademark &amp; Licensing</span>
    </div>

    <div class="divider"></div>

    <address class="address">
      437 E. Alder Rd.<br>
      Larkfield, ND 58408
    </address>

    <ul class="contact-list">
      <li>
        <svg viewBox="0 0 24 24" aria-hidden="true"><path fill="var(--icon)" d="M6.6 2.5l3 3.4-1.8 2.4c1.2 2.7 3.3 4.8 6 6l2.4-1.8 3.4 3-1.6 3.6C10.6 19.4 4.6 13.4 3 5.2z"/></svg>
        701-555-0173
      </li>
      <li>
        <svg viewBox="0 0 24 24" aria-hidden="true"><rect x="6" y="2" width="12" height="20" rx="2" fill="var(--icon)"/><rect x="8" y="5" width="8" height="11" fill="#fff"/></svg>
        701-555-0145
      </li>
      <li>
        <svg viewBox="0 0 24 24" aria-hidden="true"><circle cx="12" cy="12" r="4" fill="none" stroke="var(--icon)" stroke-width="2.4"/><path d="M16 8v5.5a2.5 2.5 0 0 0 5 0V12a9 9 0 1 0-4 7.5" fill="none" stroke="var(--icon)" stroke-width="2.4"/></svg>
        Piet.Morrow@korvelmarks.example
      </li>
      <li>
        <svg viewBox="0 0 24 24" aria-hidden="true"><circle cx="12" cy="12" r="9.5" fill="none" stroke="var(--icon)" stroke-width="2"/><ellipse cx="12" cy="12" rx="4" ry="9.5" fill="none" stroke="var(--icon)" stroke-width="1.6"/><path d="M2.5 12h19M4 7h16M4 17h16" stroke="var(--icon)" stroke-width="1.4"/></svg>
        www.korvelmarks.example
      </li>
    </ul>

    <div class="band-rule"></div>
    <div class="name-band">
      <div class="person-name">Piet Morrow</div>
      <div class="person-title">VP of Technology</div>
    </div>
  </article>
</body>
</html>
```